Blind dating / hook up web

We're creating a new web application based on blind dates to hook up with others who like you (occasional dating, not long-term relationships): www.velvetquorra.com
The background idea is the same as other dating websites (there're many differences but probably don't matter for the design): to browse potential matching profiles based on several criteria (age, gender, zone, etc.) and vote for the ones you like (a yes/no answer just seeing the pictures and basic info, option to see the detailed profile including other users feedback about that profile). The other users do the same, and then, you can see the real matches and contact them.
The one who start the contact to matched profiles, should pay for it, discounting the cost from a previously funded credit balance.
There's also a section to browse for meeting places/plans suggestions.
After you had any date, you could leave feedback about the other, so, everyone had a reputation (similar to the Trandel's feedback system).
Of course, the other typical options: register/mail verification, profile edit, "loading..." stuff, etc.
We'll start with a typical website application, but we'll move to mobile app soon, so, a responsive design will be a plus.

We expect to get a design to use as a pattern to develop (our job) the application, so, we'll need to work with the winning designer to get the graphical pieces/elements (backgrounds, icons, sprites, etc.) not only the whole screen captures. We'll contact the finalists to discuss details about how much of this are included or not and possible future work if we need it.

We've got no previous work done on logos or color schemes, so, feel free to work on whatever you want.

Please, feel free to ask for details if you need more: plomworks@mivrano.net
Updates

One preference on our web development will be to use Bootstrap (or similar frameworks), so, if you know about it and you'd like to take in care, this will be a plus, not a must. If you think there will be something to gain on other design patterns, please, forget Bootstrap and put preference on the design itself.

After received the first drafts, I think there's something general to clarify:

Everybody seem to tend to include several romantic references... the website will not be dedicated to find a long term relationship but occasional affairs, so, maybe hearts aren't the best symbol and romantic pictures/slogans the best resources. 
Also we're searching for a different design/concept than other dating services... there're some key points to make it special (different from typical date websites): 
- Mark potential matching profiles with answering a simply Yes/No (I like / I don't like) 
- Blind dates: you finally don't know who are you going to meet, you just know both answered Yes. So, intrigue will be a better idea than love. 

Let’sfocus a little more what we have in mind to be a different dating site andwhat we expect to obtain with this design project:

The mainfunctionalities and, so, the most important parts to design are:

1. Viewinga sequence of potential matching profiles, answer a question similar to “do youwant to hook up he/she/them?” Clearly more “hot” than “sweet”… more erotic (notX) than love/tender… more prohibited/hidden/secret thanstandard/traditional/public/familiar…

This simplysystem can be the principal idea so, could take a good place in the home,before register showing the best rated profiles, and after register to show thepotential matches.

The sitewon’t be restricted to men/women, it will allow to register as couple too andthe mix of sexual orientations hetero/bi/homo... Of course you should registerand choose your filter parameters, but you’ll do it sometimes, not in everyvisit to the site.

The usershould see a big picture of each profile (this is the first attraction, we’rehooking up not searching for our whole-life partner) and just a few otherdetails like age and feedback rating from other users that already met thatprofile.

Thereshould be a way to review what profiles did you answer Yes and what No.

2. Anotherimportant part of the site is the one to create and propose meet plans. You canpost here your fantasies, your plans, your suggestions about what do you wantto do or what you propose for the meeting. This is where the search engine willtake place, to propose you places, ideas or services based on what you’refinding. This will be some kind of wizard or assistant, to “configure” yourideal meeting. It should suggest you activities to include in your plan and thesearch engine will suggest related places related to that activities. I.e.: ifI’d like to take a dinner, grab some beers and finish the night on a 5 starhotel suite, I’ll add “Dinner ideas”, “going out ideas” and “night stay ideas”(or something similar) and the engine will suggest me some near restaurants,pubs and hotels. Of course, you can enter your personalized plan manually inplain text or just select activities without taking any suggestion. (reserve aplace to suggest new activities to the system!)

Afterconfiguring your plan, you can post it to be realized some days and expose itto your matches to find anyone that like your plan.

This wizardwill allow you to browse the past plans to edit/reuse them and also receiveanswers from the matching profiles who like your plant to initiate the finalcontact and meet them.

3. Inanother section you should see plans posted by others and have the way toaccept or discard them.

4. Ofcourse, the homepage must not be as simple as the Yes/No answering section, it’simportant to explain what the service are and how it works, but, for us, it’smore important to see how the “daily” operative will show up than the home,because the home must be a reflect, a summary, of the operative surrounded bycatching slogans.

There’realso several related or secondary screens and resources to be designed, but,first, we’ll to focus on these four things. Drafts should reflect these ideasor will be very difficult to fit.

After revising a lot of designs sent, there's something we're doing wrong... maybe I'm not explaining myself well, so, let me try again to expose some important ideas and add some others that had appeared after a few designs that I thing they're on the right way:

- the site should be different from the "standard" dating services. Think more in casual meetings, sex encounters, swingers, hot nights, etc. Men, women or couples (even groups!) looking for anything... so, think on any kind of sexual orientation. People live in a stressed society, they're finding something different without loosing time... something spicy, intrigue, surprise, horny... just fun, not love, no sweet, no false promises... but at the same time, think on another way to structure it, another point of view, not the typical Register, browse, contact, meet.
- please, avoid the "register" form directly on the home... the user should take a full free tour all over the site without registering. The site will collect information about his/her/their preferences while he/she/they are looking what the site is about. When clicking on something that really need to be registered, then, the register form will appear already filled with all the collected information. Some kind of remember should appear if the user is using the site for a long time stuck, for example, answering yes/no to the profiles. But there shouldn't be any pressure to register, it should be a natural need after a while.
- The landing homepage should accomplish just three main objectives:
1. Explain what the service are about in just a few sentences (more about it later)
2. Choose your profile type preferences (I'm looking for...): men/women/couples, taking in care that I could find one, two or all three options... and enter to the site to see profiles
3. If I'm already registered, log in.
The login should be easy to see and find, but shouldn't be take too much importance.
The explaining sentences/section should be also easy to see, but can be a scroll down section
The most important and eye-catching should be the selector... with naughty pictures of men/women/couples to mark what you're looking for... maybe a title "What are you looking for?" and a site entrance "Let's hook-up!" that appears after choosing at least one option...
- After the landing homepage, the operational sections described on the previous update... where the backgrounds (and maybe the whole theme) should change according the user preferences... (don't show a women picture if the user isn't looking for women).
Don't think about if the design will end in a very difficult development! it's more important to have a good design and then, our developers will find the way to implement it. Don't be afraid of it! let your talent flow freely ;)

Many of your are using some kind of form to enter the search parameters... We want to try to avoid this and we're thinking on integrate the form on the homepage itself... something like to use icons to select "what I'm" (Man/Woman/Couple... in a similar way as many of you are showing the total profiles of each...); then, a second, bigger, selector to choose "what I'm looking for" (Men/Women/Couples, could select one or many)... maybe playing with big pictures or the background itself; finally (perhaps integrated with the results) some kind of slider to select the age range, leaving only the dropdowns to select the geographic location (if no one has a better idea with no typical "fields").

Industry/Entity Type

Dating

```html
<!DOCTYPE html>
<html lang="en">
<head>
<meta charset="utf-8">
<title>Velvetquorra — Blind Dates</title>
<link href="https://fonts.googleapis.com/css2?family=Open+Sans:wght@400;600;700&display=swap" rel="stylesheet">
<style>
:root{
  --red:#c3161c;
  --red-dark:#8e0c10;
  --red-deep:#6e080b;
  --field:#a00f14;
  --blue:#1aa0dc;
  --ink:#555;
  --ink-soft:#888;
  --grey-band:#ededed;
  --footer:#1e1e1e;
  --footer-line:#2c2c2c;
  --white:#fff;
}
*{box-sizing:border-box;margin:0;padding:0}
html,body{width:855px;height:1200px;overflow:hidden}
body{font-family:'Open Sans',Arial,sans-serif;color:var(--ink);background:var(--white);position:relative}

.topbar{height:30px;background:var(--red-deep);display:flex;align-items:center;justify-content:space-between;padding:0 30px}
.brand{color:var(--white);font-weight:700;font-size:17px}
.top-actions{display:flex;align-items:center;gap:10px}
.member-login{font-size:9px;color:var(--white);display:flex;align-items:center;gap:5px}
.member-login .dot{width:8px;height:8px;background:var(--white);border-radius:50%}
.lang{display:flex;align-items:center;gap:4px;font-size:9px;color:var(--white)}
.lang .square{width:12px;height:8px;background:var(--white)}

.hero{position:relative;height:432px;background:linear-gradient(100deg,#d8d2cc 0%,#f1ece6 35%,#e6ddd2 60%,#cfc7bd 100%)}
.hero-photo{position:absolute;left:0;top:0;width:100%;height:100%;background:radial-gradient(ellipse at 30% 45%,#e9c7ad 0%,#dcbfa8 18%,rgba(240,234,226,0) 45%)}
.join-panel{position:absolute;left:490px;top:30px;width:336px;height:320px;background:var(--red);padding:14px 26px;color:var(--white)}
.join-panel h2{text-align:center;font-weight:600;font-size:22px;margin-bottom:10px}
.row{display:flex;gap:6px;margin-bottom:9px}
.field{background:var(--field);height:30px;display:flex;align-items:center;justify-content:space-between;padding:0 9px;font-size:10px;color:#f3cfd0;flex:1}
.field .caret{width:0;height:0;border-left:4px solid transparent;border-right:4px solid transparent;border-top:5px solid #f3cfd0}
.field.small{height:24px;font-size:9px}
.join-btn{position:absolute;left:490px;top:360px;width:336px;height:42px;background:var(--blue);color:var(--white);font-size:20px;font-weight:600;display:flex;align-items:center;justify-content:center}
.terms{position:absolute;left:490px;top:410px;width:336px;text-align:center;font-size:8px;color:#a22}

.intro{height:275px;text-align:center;padding-top:25px;position:relative}
.intro-map{position:absolute;left:200px;top:70px;width:455px;height:190px;background:radial-gradient(ellipse,#f1f1f1 0%,#f7f7f7 55%,rgba(255,255,255,0) 75%)}
.section-title{color:var(--red);font-size:23px;font-weight:600}
.lead{font-size:10.5px;line-height:1.6;color:var(--ink-soft);width:600px;margin:10px auto 0}
.stats{position:relative;display:flex;justify-content:center;gap:95px;margin-top:40px}
.stat{width:90px;display:flex;flex-direction:column;align-items:center}
.stat svg{height:56px}
.stat .num{font-size:18px;color:#333;margin-top:14px}
.stat .label{font-size:9px;color:var(--ink-soft);margin-top:3px}

.blind-dates{background:var(--grey-band);height:245px;margin-top:12px;text-align:center;padding-top:15px}
.profiles{display:flex;justify-content:center;gap:25px;margin-top:30px}
.profile{width:58px;display:flex;flex-direction:column;align-items:center}
.avatar{width:58px;height:58px;border-radius:50%;border:3px solid var(--white)}
.name{font-size:10px;color:#333;margin-top:6px}
.meta{font-size:7px;color:var(--ink-soft);line-height:1.3;margin-top:2px}
.vote{display:flex;gap:3px;margin-top:6px}
.vote span{width:26px;height:11px;font-size:7px;color:var(--white);display:flex;align-items:center;justify-content:center}
.yes{background:var(--red)}
.no{background:var(--blue)}

.feedback{position:absolute;left:0;top:1010px;width:855px;height:65px;background:var(--red);display:flex;align-items:center;padding:0 100px;gap:14px}
.feedback p{color:var(--white);font-size:17px;flex:1}
.feedback .input{width:200px;height:28px;background:var(--white);font-size:9px;color:#aaa;display:flex;align-items:center;padding-left:10px}
.feedback .submit{width:120px;height:28px;background:var(--red-dark);color:var(--white);font-size:12px;display:flex;align-items:center;justify-content:center}

.footer{position:absolute;left:0;top:1075px;width:855px;height:125px;background:var(--footer);padding:22px 100px 0;color:#ccc}
.footer-row{display:flex;justify-content:space-between}
.footer h4{font-size:11px;font-weight:600;color:var(--white)}
.links{display:flex;gap:18px;font-size:8.5px;margin-top:26px}
.social{display:flex;gap:7px;margin-top:26px}
.social span{width:15px;height:15px;border-radius:50%;background:#bbb}
.copyright{border-top:1px solid var(--footer-line);margin-top:18px;padding-top:9px;font-size:7.5px;color:#888}
</style>
</head>
<body>

<header class="topbar">
  <div class="brand">Velvetquorra</div>
  <div class="top-actions">
    <div class="member-login"><span class="dot"></span>Member Login</div>
    <div class="lang"><span class="square"></span>EN</div>
  </div>
</header>

<section class="hero">
  <div class="hero-photo" role="img" aria-label="Smiling young woman looking at her phone"></div>
  <form class="join-panel">
    <h2>Join us</h2>
    <div class="row">
      <div class="field small">I am <span class="caret"></span></div>
      <div class="field small">Looking for <span class="caret"></span></div>
    </div>
    <div class="row">
      <div class="field">Month <span class="caret"></span></div>
      <div class="field">Day <span class="caret"></span></div>
      <div class="field">Year <span class="caret"></span></div>
    </div>
    <div class="row"><div class="field">Country <span class="caret"></span></div></div>
    <div class="row"><div class="field">Enter your username</div></div>
    <div class="row"><div class="field">Enter your Password</div></div>
  </form>
  <div class="join-btn">Join Now!</div>
  <div class="terms">By clicking Join Now you are agreeing to our Terms &amp; Conditions</div>
</section>

<section class="intro">
  <div class="intro-map" role="img" aria-label="Faint world map"></div>
  <h2 class="section-title" style="position:relative">It all starts with a Date</h2>
  <p class="lead" style="position:relative">You find us, finally, and you are already in love. More than 2.000.000 around the world already shared the same experience and now our system is waiting to make it just get easier!</p>
  <div class="stats">
    <div class="stat">
      <svg viewBox="0 0 60 56" width="60"><path d="M18 22c-4-8-16-6-15 3 1 8 15 16 15 16s14-8 15-16c1-9-11-11-15-3z" fill="#c3161c"/><path d="M40 14c-4-8-16-6-15 3 1 8 15 16 15 16s14-8 15-16c1-9-11-11-15-3z" fill="#1aa0dc"/><rect x="12" y="44" width="36" height="4" fill="#c3161c"/></svg>
      <div class="num">20000</div><div class="label">Members in total</div>
    </div>
    <div class="stat">
      <svg viewBox="0 0 60 56" width="60"><circle cx="22" cy="14" r="9" fill="#c3161c"/><path d="M6 52c0-14 8-22 16-22s16 8 16 22z" fill="#c3161c"/><circle cx="42" cy="20" r="8" fill="#1aa0dc"/><path d="M30 52c0-12 6-18 12-18s12 6 12 18z" fill="#1aa0dc"/></svg>
      <div class="num">4567</div><div class="label">Members online</div>
    </div>
    <div class="stat">
      <svg viewBox="0 0 40 56" width="40"><circle cx="20" cy="17" r="12" fill="none" stroke="#c3161c" stroke-width="6"/><path d="M20 29v24M11 43h18" stroke="#c3161c" stroke-width="6"/></svg>
      <div class="num">2022</div><div class="label">Women online</div>
    </div>
    <div class="stat">
      <svg viewBox="0 0 50 56" width="50"><circle cx="20" cy="36" r="13" fill="none" stroke="#1aa0dc" stroke-width="6"/><path d="M29 27l14-14M30 11h14v14" fill="none" stroke="#1aa0dc" stroke-width="6"/></svg>
      <div class="num">2726</div><div class="label">Men online</div>
    </div>
  </div>
</section>

<section class="blind-dates">
  <h2 class="section-title">Blind Dates</h2>
  <p class="lead">You can register and create your profile for FREE you finally don't know who you are going to meet, you just know both answered Yes. So, intrigue will be a better idea than love.</p>
  <div class="profiles">
    <div class="profile"><div class="avatar" role="img" aria-label="Member profile photo" style="background:#b08a6e"></div><div class="name">Anthony</div><div class="meta">Registered 1 hours<br>15 minutes ago</div><div class="vote"><span class="yes">Yes</span><span class="no">No</span></div></div>
    <div class="profile"><div class="avatar" role="img" aria-label="Member profile photo" style="background:#7a5b48"></div><div class="name">joe/kel</div><div class="meta">Registered 2 hours<br>10 minutes ago</div><div class="vote"><span class="yes">Yes</span><span class="no">No</span></div></div>
    <div class="profile"><div class="avatar" role="img" aria-label="Member profile photo" style="background:#c9a48b"></div><div class="name">Anthony</div><div class="meta">Registered 1 hours<br>15 minutes ago</div><div class="vote"><span class="yes">Yes</span><span class="no">No</span></div></div>
    <div class="profile"><div class="avatar" role="img" aria-label="Member profile photo" style="background:#8c6a56"></div><div class="name">joe/kel</div><div class="meta">Registered 3 hours<br>20 minutes ago</div><div class="vote"><span class="yes">Yes</span><span class="no">No</span></div></div>
    <div class="profile"><div class="avatar" role="img" aria-label="Member profile photo" style="background:#a2785e"></div><div class="name">Anthony</div><div class="meta">Registered 1 hours<br>15 minutes ago</div><div class="vote"><span class="yes">Yes</span><span class="no">No</span></div></div>
    <div class="profile"><div class="avatar" role="img" aria-label="Member profile photo" style="background:#6d5042"></div><div class="name">joe/kel</div><div class="meta">Registered 2 hours<br>40 minutes ago</div><div class="vote"><span class="yes">Yes</span><span class="no">No</span></div></div>
    <div class="profile"><div class="avatar" role="img" aria-label="Member profile photo" style="background:#bf9a80"></div><div class="name">Anthony</div><div class="meta">Registered 1 hours<br>15 minutes ago</div><div class="vote"><span class="yes">Yes</span><span class="no">No</span></div></div>
    <div class="profile"><div class="avatar" role="img" aria-label="Member profile photo" style="background:#94705a"></div><div class="name">joe/kel</div><div class="meta">Registered 4 hours<br>5 minutes ago</div><div class="vote"><span class="yes">Yes</span><span class="no">No</span></div></div>
  </div>
</section>

<section class="feedback">
  <p>you could leave feedback about the other</p>
  <div class="input">Write your feedback</div>
  <div class="submit">Submit</div>
</section>

<footer class="footer">
  <div class="footer-row">
    <div>
      <h4>Quick links</h4>
      <nav class="links"><span>About</span><span>Terms of Use</span><span>Privacy</span><span>Cookies</span><span>FAQ</span><span>Contacts</span><span>Jobs</span><span>Affiliates</span></nav>
    </div>
    <div>
      <h4>Follow us on</h4>
      <div class="social"><span></span><span></span><span></span><span></span><span></span><span></span></div>
    </div>
  </div>
  <div class="copyright">© 2014. All Rights Reserved</div>
</footer>

</body>
</html>
```